Kelvaro, The smart answer for charity drives

Kelvaro needs a simple Wordpress website development. The key message is that we have three wins in fundraising according to my services - win for theorganisation - win for the partner and win for the audience and the community.STYLE:- My business card is attached so the site colors could match with the card;- We love the style of this website: https://www.marenboltwick.co.nz/ because it is modern, minimalist, clean and easy to navigate. I am happy to have a similar parallax (scrolling) site as the reference samplePlease feature the following on the site:* INTRODUCTION (or About)* SERVICES* MY QUOTE* CONTACT US* PLAXTERN ( the contents are in the attached .rtf file - please message me if you are unable to open this document)Deliverables:- I would like a fully functioning (Coded) wordpress site

• Personable approach
• It is all about You (the other person who is approach my business)

```html
<!DOCTYPE html>
<html lang="en">
<head>
<meta charset="utf-8">
<title>Kelvaro — The smart answer for charity drives</title>
<link href="https://fonts.googleapis.com/css2?family=Playfair+Display:ital,wght@0,400;1,400&family=Lato:wght@400;700&display=swap" rel="stylesheet">
<style>
:root{
  --canvas:#ffffff;
  --intro-bg:#f0f0f0;
  --ink:#2b2b2b;
  --body:#6a6a6a;
  --rule:#cfcfcf;
  --services-a:#6c6169;
  --services-b:#4d434d;
  --blush:#e3b2a6;
  --blush-soft:#f4cfc6;
  --quote-bg:#fbfbfb;
  --taupe:#a68b74;
  --white:#ffffff;
  --field:#ffffff;
  --submit:#d9a69a;
}
*{margin:0;padding:0;box-sizing:border-box}
html,body{width:1200px;height:1200px;overflow:hidden;background:var(--canvas)}
body{position:relative;font-family:'Lato',sans-serif}
.site{position:absolute;left:406px;top:0;width:389px;height:1200px;overflow:hidden}
.abs{position:absolute}

/* hero */
.hero{left:0;top:0;width:389px;height:248px}
.hero-photo{position:absolute;inset:0;background:linear-gradient(160deg,#8d8a88 0%,#6e625a 35%,#8a6a52 60%,#4a3c35 100%)}
.hero-shade{position:absolute;inset:0;background:linear-gradient(90deg,rgba(40,32,28,.45),rgba(40,32,28,0) 60%)}
.brand{left:35px;top:6px;font-weight:400;font-size:22px;color:var(--white);letter-spacing:.2px}
.nav{top:17px;font-size:5px;font-weight:700;color:var(--white);letter-spacing:.1px}
.hero-rule{left:35px;width:160px;height:0;border-top:.6px solid rgba(255,255,255,.7)}
.hero-title{left:35px;top:84px;width:160px;text-align:center;font-family:'Playfair Display',serif;font-weight:400;font-size:16px;line-height:20px;color:var(--white)}
.hero-contact{left:35px;font-size:4.4px;color:var(--white);display:flex;align-items:center;gap:4px}
.hero-contact svg{width:5px;height:5px;fill:var(--white)}

/* intro */
.intro{left:0;top:248px;width:389px;height:347px;background:var(--intro-bg)}
.section-title{font-family:'Playfair Display',serif;font-weight:400;font-size:17px;color:var(--ink);letter-spacing:.3px}
.section-rule{height:0;border-top:.6px solid #9a9a9a}
.copy{left:34px;width:316px;font-size:4.3px;line-height:7.2px;color:var(--body)}
.pull{left:34px;width:316px;text-align:center;font-family:'Playfair Display',serif;font-size:8.6px;line-height:14px;color:#4a4a4a}
.thin{left:34px;width:316px;border-top:.6px solid var(--rule)}

/* services */
.services{left:0;top:595px;width:389px;height:245px}
.services-bg{position:absolute;inset:0;background:radial-gradient(circle at 30% 40%,var(--services-a),var(--services-b) 75%)}
.service-list{left:50px;top:652px;list-style:none;font-size:5.2px;font-weight:700;color:var(--white)}
.service-list li{height:11.7px;display:flex;align-items:center;gap:6px}
.service-list svg{width:5px;height:4px;stroke:var(--white);fill:none;stroke-width:1}
.services-photo{left:194px;top:654px;width:158px;height:137px;background:linear-gradient(135deg,#3e3530 0%,#7a6656 45%,#c9bfb4 70%,#54473f 100%);box-shadow:0 1px 3px rgba(0,0,0,.3)}

/* quote */
.quote-mark{font-family:'Playfair Display',serif;font-size:72px;line-height:1;color:var(--blush-soft)}
.quote-text{left:34px;top:898px;width:320px;text-align:center;font-family:'Playfair Display',serif;font-style:italic;font-size:9px;line-height:14.4px;color:#3a3a3a}

/* contact */
.contact{left:0;top:990px;width:389px;height:210px;background:var(--taupe)}
.contact-title{left:0;top:1008px;width:389px;text-align:center;font-family:'Playfair Display',serif;font-weight:400;font-size:16px;color:var(--white)}
.label{font-size:6px;font-weight:700;color:var(--white)}
.field{background:var(--field);font-size:3.8px;color:#8a8a8a;padding:3px 4px}
.submit{left:195px;top:1143px;width:34px;height:14px;background:var(--submit);font-size:3.6px;color:#6b4a42;display:flex;align-items:center;justify-content:center}
.info{left:252px;display:flex;gap:7px;font-size:4.4px;line-height:7px;color:var(--white)}
.info .badge{width:10px;height:10px;border-radius:50%;border:.6px solid rgba(255,255,255,.8);display:flex;align-items:center;justify-content:center;flex:none}
.info svg{width:4.5px;height:4.5px;fill:var(--white)}
.footer-rule{left:38px;top:1176px;width:316px;border-top:.5px solid rgba(255,255,255,.5)}
.footer-note{left:0;top:1187px;width:389px;text-align:center;font-size:3.4px;color:var(--white)}
.to-top{left:359px;top:1160px;width:23px;height:22px;background:rgba(255,255,255,.85);display:flex;align-items:center;justify-content:center}
.to-top svg{width:13px;height:8px;stroke:#777;fill:none;stroke-width:1}
</style>
</head>
<body>
<div class="site">

  <header class="abs hero">
    <div class="hero-photo" role="img" aria-label="Photo of a group of smiling young people stacking their hands together in the centre"></div>
    <div class="hero-shade"></div>
  </header>
  <div class="abs brand">Kelvaro</div>
  <nav>
    <span class="abs nav" style="left:212px">ABOUT</span>
    <span class="abs nav" style="left:242px">SERVICES</span>
    <span class="abs nav" style="left:280px">MY QUOTE</span>
    <span class="abs nav" style="left:321px">CONTACT US</span>
  </nav>
  <div class="abs hero-rule" style="top:78px"></div>
  <h1 class="abs hero-title">The Smart Answer<br>for Charity Drives</h1>
  <div class="abs hero-rule" style="top:132px"></div>
  <div class="abs hero-contact" style="top:153px">Mira Dellanova-Price, MDipl, BIntSt, B.Sc Kelvaro</div>
  <div class="abs hero-contact" style="top:164px"><svg viewBox="0 0 10 10"><path d="M5 0a3.5 3.5 0 0 0-3.5 3.5C1.5 6 5 10 5 10s3.5-4 3.5-6.5A3.5 3.5 0 0 0 5 0zm0 5a1.5 1.5 0 1 1 0-3 1.5 1.5 0 0 1 0 3z"/></svg>418 Harbour Lane, Seacliff, 0741, Auckland</div>
  <div class="abs hero-contact" style="top:175px"><svg viewBox="0 0 10 10"><path d="M2 0l2 2.5-1.2 1.4a6 6 0 0 0 3.3 3.3L7.5 6 10 8l-1.5 2C4 10 0 6 0 1.5z"/></svg>021 73 19 62</div>
  <div class="abs hero-contact" style="top:186px"><svg viewBox="0 0 10 10"><path d="M0 2h10v6H0zM0 2l5 3.5L10 2" stroke="#6e625a" stroke-width=".6"/></svg>mira@kelvaro.co.nz</div>

  <section class="abs intro"></section>
  <h2 class="abs section-title" style="left:35px;top:263px">INTRODUCTION</h2>
  <div class="abs section-rule" style="left:35px;top:285px;width:120px"></div>
  <p class="abs copy" style="top:292px">I grew up in a small coastal town where I finished my degree in political studies and global affairs. I then moved abroad to continue my studies, and completed a master's degree in diplomacy and public relations.</p>
  <p class="abs copy" style="top:314px">Further learning includes short courses in board governance and contract law, a certificate in nonprofit leadership and a recent online programme on strategy, change and growth for community organisations.</p>
  <p class="abs copy" style="top:335px">I worked on the organising team of a major international sporting event, looking after visiting national committees and their delegations as deputy manager in the relations department.</p>
  <p class="abs copy" style="top:357px">I moved to New Zealand after the event and worked for a city council as sponsorship manager of festivals and community events. Later I led a regional sports body as executive officer for two years, and held contracts through my own sponsorship and marketing business with charities, sports clubs, health trusts, housing groups, councils and other organisations. A few years ago I worked for a city council as partnership manager for major projects, exceeding a multi-million dollar target for a public gardens development within eighteen months, and raising further funds for a river plan and a series of new playgrounds for future generations across the wider region and its towns.</p>
  <p class="abs copy" style="top:407px">My most recent role before starting my own business again was director of philanthropy for a city museum, where I was responsible for giving and legacy programmes and developed a new bequest scheme called Roots for Tomorrow.</p>
  <p class="abs copy" style="top:429px">I hold New Zealand citizenship.</p>
  <div class="abs thin" style="top:452px"></div>
  <p class="abs pull" style="top:458px">I am passionate about my family, community sport,<br>enjoy music, cooking for friends and travelling.</p>
  <div class="abs thin" style="top:497px"></div>
  <p class="abs copy" style="top:509px">I have governance experience with several local trusts and school boards, and served as president of a cultural community group for five years. I am a current member of two director and leadership networks.</p>
  <p class="abs copy" style="top:530px">My greatest passion is people. I am grateful to all the teams I have worked with and the results we achieved together. I always meet with potential partners to identify their objectives and outcomes, then tailor proposals to fit their desires, the project's aims and the community's interests. My approach is tailored and very personal. I believe this is the point of difference, and it has built strong relationships with funders, businesses and donors over many years.</p>
  <p class="abs copy" style="top:566px">I am excited with projects that have an impact in the community and in our country.</p>

  <section class="abs services">
    <div class="services-bg" role="img" aria-label="Faded photo of runners' shoes in motion behind a dusky purple overlay"></div>
  </section>
  <h2 class="abs section-title" style="left:35px;top:616px;color:var(--white)">SERVICES</h2>
  <div class="abs section-rule" style="left:35px;top:637px;width:80px;border-color:rgba(255,255,255,.7)"></div>
  <ul class="abs service-list">
    <li><svg viewBox="0 0 10 8"><path d="M0 4h9M6 1l3 3-3 3"/></svg>Fundraising Strategic Action Plans</li>
    <li><svg viewBox="0 0 10 8"><path d="M0 4h9M6 1l3 3-3 3"/></svg>Marketing Plans</li>
    <li><svg viewBox="0 0 10 8"><path d="M0 4h9M6 1l3 3-3 3"/></svg>Workshops on fundraising</li>
    <li><svg viewBox="0 0 10 8"><path d="M0 4h9M6 1l3 3-3 3"/></svg>Evaluation on fundraising projects</li>
    <li><svg viewBox="0 0 10 8"><path d="M0 4h9M6 1l3 3-3 3"/></svg>Funding applications</li>
    <li><svg viewBox="0 0 10 8"><path d="M0 4h9M6 1l3 3-3 3"/></svg>Commercial partnerships</li>
    <li><svg viewBox="0 0 10 8"><path d="M0 4h9M6 1l3 3-3 3"/></svg>Giving Programmes</li>
    <li><svg viewBox="0 0 10 8"><path d="M0 4h9M6 1l3 3-3 3"/></svg>Legacy Programmes</li>
    <li><svg viewBox="0 0 10 8"><path d="M0 4h9M6 1l3 3-3 3"/></svg>Capital Projects Fundraising</li>
    <li><svg viewBox="0 0 10 8"><path d="M0 4h9M6 1l3 3-3 3"/></svg>Feasibility Studies</li>
    <li><svg viewBox="0 0 10 8"><path d="M0 4h9M6 1l3 3-3 3"/></svg>Consultancy on fundraising</li>
    <li><svg viewBox="0 0 10 8"><path d="M0 4h9M6 1l3 3-3 3"/></svg>Mentoring on fundraising</li>
  </ul>
  <div class="abs services-photo" role="img" aria-label="Photo of hands at a laptop showing a fundraising screen, with sticky notes and a calculator on the desk"></div>

  <svg class="abs" style="left:0;top:800px" width="389" height="190" viewBox="0 0 389 190" aria-hidden="true">
    <path d="M0 12 Q194.5 50 389 12 L389 190 L0 190 Z" fill="var(--quote-bg)"/>
    <path d="M0 12 Q194.5 50 389 12" fill="none" stroke="var(--blush)" stroke-width="2.2"/>
  </svg>
  <div class="abs quote-mark" style="left:32px;top:834px">&ldquo;</div>
  <p class="abs quote-text">'I look forward to working with you and your team and together achieving results<br>that will make a difference where we live'.</p>
  <div class="abs quote-mark" style="left:313px;top:918px">&rdquo;</div>

  <section class="abs contact"></section>
  <h2 class="abs contact-title">CONTACT US</h2>
  <div class="abs section-rule" style="left:145px;top:1031px;width:99px;border-color:rgba(255,255,255,.7)"></div>
  <div class="abs label" style="left:38px;top:1050px">Contact Form</div>
  <div class="abs field" style="left:38px;top:1068px;width:91px;height:15px">Name:</div>
  <div class="abs field" style="left:138px;top:1068px;width:91px;height:15px">Phone No.</div>
  <div class="abs field" style="left:38px;top:1088px;width:191px;height:15px">Address:</div>
  <div class="abs field" style="left:38px;top:1108px;width:191px;height:27px">Message:</div>
  <div class="abs submit">SUBMIT</div>

  <div class="abs label" style="left:252px;top:1050px">Contact Information</div>
  <div class="abs info" style="top:1065px"><span class="badge"><svg viewBox="0 0 10 10"><path d="M5 0a3.5 3.5 0 0 0-3.5 3.5C1.5 6 5 10 5 10s3.5-4 3.5-6.5A3.5 3.5 0 0 0 5 0zm0 5a1.5 1.5 0 1 1 0-3 1.5 1.5 0 0 1 0 3z"/></svg></span><span>418 Harbour Lane,<br>Seacliff, 0741, Auckland</span></div>
  <div class="abs info" style="top:1086px"><span class="badge"><svg viewBox="0 0 10 10"><path d="M2 0l2 2.5-1.2 1.4a6 6 0 0 0 3.3 3.3L7.5 6 10 8l-1.5 2C4 10 0 6 0 1.5z"/></svg></span><span style="padding-top:1.5px">021 73 19 62</span></div>
  <div class="abs info" style="top:1107px"><span class="badge"><svg viewBox="0 0 10 10"><path d="M0 2h10v6H0zM0 2l5 3.5L10 2" stroke="#a68b74" stroke-width=".6"/></svg></span><span style="padding-top:1.5px">mira@kelvaro.co.nz</span></div>
  <div class="abs label" style="left:252px;top:1129px">Plaxtern:</div>
  <div class="abs info" style="top:1142px"><span class="badge"></span></div>

  <div class="abs footer-rule"></div>
  <div class="abs footer-note">© 2019 KELVARO. All rights reserved. &nbsp;|&nbsp; TERMS OF SERVICE &nbsp;|&nbsp; PRIVACY POLICY</div>
  <div class="abs to-top"><svg viewBox="0 0 13 8"><path d="M1 7l5.5-5.5L12 7"/></svg></div>

</div>
</body>
</html>
```